Need a business cards for a hair dressing salon.

Target Market(s)

Target woman for Hair cuts, bridal makeup, occasion, fashion makeup and etc.

Industry/Entity Type

Hair

Font styles to use
Serif
Script

Requirements
Must have
• - Business card to be memorable and recognizable

- Please include the following on the business card:
- Business name: Salon Orimba
- Name: Kalini Desmodo (Name Must be changeable)
- Occupation: Hair Dresser & Beautician
- Contact number: 04 739 2 HAIR
- Email: mail@orimba.com.au
- Facebook (please use image): www.facebook.com/orimba.com.au
Nice to have
• Font Styles:
Business Name - Script
Other Text - Serif

```html
<!DOCTYPE html>
<html lang="en">
<head>
<meta charset="utf-8">
<title>Salon Orimba – Business Card</title>
<link rel="stylesheet" href="https://fonts.googleapis.com/css2?family=Dancing+Script:wght@700&family=Lora:wght@400;700&display=swap">
<style>
  :root {
    --backdrop: #1b1b1c;
    --card-black: #060607;
    --portrait-light: #8a8a8c;
    --portrait-mid: #3d3d40;
    --portrait-dark: #111113;
    --gold: #d9b65a;
    --white: #f2f2f2;
    --soft-grey: #b9b9bb;
    --band: rgba(0, 0, 0, 0.55);
  }
  html, body {
    margin: 0;
    padding: 0;
    width: 1200px;
    height: 900px;
    overflow: hidden;
    background: var(--backdrop);
  }
  .card {
    position: absolute;
    left: 110px;
    top: 170px;
    width: 980px;
    height: 560px;
    border-radius: 26px;
    overflow: hidden;
    background: var(--card-black);
    box-shadow: 0 20px 50px rgba(0, 0, 0, 0.6);
    font-family: "Lora", serif;
  }
  .portrait-area {
    position: absolute;
    left: 0;
    top: 0;
    width: 700px;
    height: 560px;
    background:
      radial-gradient(ellipse 220px 260px at 320px 250px, var(--portrait-light) 0%, var(--portrait-mid) 55%, transparent 100%),
      linear-gradient(90deg, var(--portrait-mid) 0%, var(--portrait-dark) 70%, var(--card-black) 100%);
  }
  .salon-name {
    position: absolute;
    right: 70px;
    top: 42px;
    margin: 0;
    font-family: "Dancing Script", cursive;
    font-weight: 700;
    font-size: 50px;
    color: var(--gold);
  }
  .stylist {
    position: absolute;
    right: 70px;
    top: 150px;
    text-align: right;
  }
  .stylist-name {
    margin: 0;
    font-weight: 700;
    font-size: 31px;
    letter-spacing: 1px;
    color: var(--white);
  }
  .stylist-role {
    margin: 2px 0 0;
    font-size: 24px;
    color: var(--gold);
  }
  .stylist-phone {
    margin: 6px 0 0;
    font-weight: 700;
    font-size: 25px;
    letter-spacing: 1px;
    color: var(--white);
  }
  .icon {
    display: inline-block;
    vertical-align: middle;
    margin-right: 8px;
  }
  .contact-band {
    position: absolute;
    left: 0;
    bottom: 0;
    width: 100%;
    height: 92px;
    background: var(--band);
    display: flex;
    align-items: center;
    justify-content: space-between;
    padding: 0 60px;
    box-sizing: border-box;
  }
  .contact-item {
    font-size: 23px;
    letter-spacing: 1px;
    color: var(--soft-grey);
  }
  .social-mark {
    display: inline-block;
    width: 16px;
    height: 16px;
    border-radius: 2px;
    background: var(--soft-grey);
    margin-right: 10px;
    vertical-align: middle;
  }
</style>
</head>
<body>
  <section class="card">
    <div class="portrait-area" role="img" aria-label="Black and white portrait of a woman with long, voluminous wavy hair"></div>

    <h1 class="salon-name">Salon Orimba</h1>

    <div class="stylist">
      <p class="stylist-name">Kalini Desmodo</p>
      <p class="stylist-role">Hair Dresser &amp; Beautician</p>
      <p class="stylist-phone">
        <svg class="icon" width="14" height="22" viewBox="0 0 14 22" aria-hidden="true">
          <rect x="1" y="1" width="12" height="20" rx="2" fill="none" stroke="#f2f2f2" stroke-width="2"/>
          <line x1="5" y1="17" x2="9" y2="17" stroke="#f2f2f2" stroke-width="2"/>
        </svg>04 739 2 HAIR(4247)
      </p>
    </div>

    <footer class="contact-band">
      <span class="contact-item">
        <svg class="icon" width="20" height="14" viewBox="0 0 20 14" aria-hidden="true">
          <rect x="0" y="0" width="20" height="14" fill="#b9b9bb"/>
          <polyline points="0,0 10,8 20,0" fill="none" stroke="#060607" stroke-width="1.6"/>
        </svg>mail@orimba.com.au
      </span>
      <span class="contact-item">
        <svg class="icon" width="20" height="20" viewBox="0 0 20 20" aria-hidden="true">
          <g fill="none" stroke="#b9b9bb" stroke-width="2.2" stroke-linecap="round">
            <path d="M8 12 L12 8"/>
            <path d="M9 5 L11 3 a3.5 3.5 0 0 1 5 5 L14 10"/>
            <path d="M11 15 L9 17 a3.5 3.5 0 0 1 -5 -5 L6 10"/>
          </g>
        </svg>www.orimba.com.au
      </span>
      <span class="contact-item"><span class="social-mark"></span>/orimba.com.au</span>
    </footer>
  </section>
</body>
</html>
```